Business card for law firm

Need business card for new law firm. Think confident, authoritative, conservative, but not stuffy or old-fashioned.

Contact Information for Business Card

Content for card - logo (uploaded), plus the following:

Paul Weybridge (larger font)
Managing Partner (larger font, but not as large as name)
Level 9, 47 Calder Lane
Sydney NSW 2000
Main Tel 02 7304 6219
Direct Tel 02 7462 3158
Email paul@wbrlegal.com.au
www.wbrlegal.com.au

Letterhead design should include logo plus:
Level 9, 47 Calder Lane
Sydney NSW 2000
Tel 02 7462 3158
www.wbrlegal.com.au

```html
<!DOCTYPE html>
<html lang="en">
<head>
<meta charset="utf-8">
<title>Weybridge Lawyers – Business Card</title>
<link rel="stylesheet" href="https://fonts.googleapis.com/css2?family=Tinos:wght@400;700&family=Arimo:wght@400&display=swap">
<style>
  :root {
    --navy: #0b2270;
    --navy-deep: #081a5a;
    --navy-soft: #14307f;
    --paper: #ffffff;
    --backdrop: #e9e6e1;
    --ink-on-navy: #ffffff;
  }
  * { box-sizing: border-box; margin: 0; padding: 0; }
  html, body { width: 1200px; height: 768px; overflow: hidden; }
  body {
    background: var(--backdrop);
    font-family: "Tinos", "Times New Roman", serif;
    position: relative;
  }
  .card {
    position: absolute;
    top: 114px;
    width: 340px;
    height: 540px;
    background: var(--paper);
    overflow: hidden;
    box-shadow: 0 6px 18px rgba(0,0,0,0.18);
  }
  .card--front { left: 220px; }
  .card--back  { left: 640px; }

  .front-field {
    position: absolute;
    inset: 0;
    background: radial-gradient(ellipse at 60% 50%, var(--navy-soft) 0%, var(--navy) 55%, var(--navy-deep) 100%);
  }

  .contact {
    position: absolute;
    left: 20px;
    top: 170px;
    width: 300px;
    text-align: center;
    color: var(--ink-on-navy);
  }
  .contact__name {
    font-size: 25px;
    letter-spacing: 0.5px;
    text-transform: uppercase;
    font-weight: 400;
    line-height: 1;
  }
  .contact__role {
    font-size: 15px;
    text-transform: uppercase;
    letter-spacing: 0.6px;
    margin-top: 4px;
  }
  .contact__rule {
    width: 40px;
    height: 1px;
    background: rgba(255,255,255,0.75);
    margin: 16px auto;
  }
  .contact__line { font-size: 15px; line-height: 1.3; }

  .brand {
    position: absolute;
    top: 200px;
    left: 0;
    width: 100%;
    text-align: center;
    color: var(--navy-deep);
  }
  .brand__mark {
    display: block;
    width: 44px;
    height: 44px;
    background: var(--navy);
    margin: 0 auto 14px;
  }
  .brand__name {
    font-size: 36px;
    letter-spacing: 1px;
    text-transform: uppercase;
    line-height: 1;
  }
  .brand__tag {
    font-size: 13px;
    letter-spacing: 11px;
    text-transform: uppercase;
    margin-top: 6px;
    padding-left: 11px;
  }

  .web-band {
    position: absolute;
    left: 0;
    top: 428px;
    width: 100%;
    height: 34px;
    background: var(--navy);
    color: var(--ink-on-navy);
    font-family: "Arimo", Arial, sans-serif;
    font-size: 14px;
    letter-spacing: 5px;
    display: flex;
    align-items: center;
    justify-content: center;
  }
  .web-line {
    position: absolute;
    left: 0;
    top: 478px;
    width: 100%;
    height: 12px;
    background: var(--navy);
  }
</style>
</head>
<body>

<section class="card card--front" aria-label="Business card front">
  <div class="front-field" role="img" aria-label="Navy decorative background with curved white accents"></div>
  <div class="contact">
    <h1 class="contact__name">Paul Weybridge</h1>
    <p class="contact__role">Managing Partner</p>
    <div class="contact__rule"></div>
    <p class="contact__line">Level 9, 47 Calder Lane</p>
    <p class="contact__line">Sydney NSW 2000</p>
    <div class="contact__rule"></div>
    <p class="contact__line">02 7304 6219 | 02 7462 3158</p>
    <p class="contact__line">paul@wbrlegal.com.au</p>
  </div>
</section>

<section class="card card--back" aria-label="Business card back">
  <div class="brand">
    <span class="brand__mark"></span>
    <p class="brand__name">Weybridge</p>
    <p class="brand__tag">Lawyers</p>
  </div>
  <div class="web-band">www.wbrlegal.com.au</div>
  <div class="web-line"></div>
</section>

</body>
</html>
```